PINE HOLLOW BUILDERS leave behind sales FLYER 8.5"x11"

We need a high quality advertising flyer 8.5"x11" for our construction company offering kitchen and bathroom remodels. Can be front and back or just the front of the flyer depending on the design. phone number to come
www.brightmortarworks.example

we are also a home inspection company. We will leave this at the home when we are done with our home inspections for our new home owners

Target Market(s)

Home owners

Industry/Entity Type

Residential Construction

Contact Information for Business Card

We want it to match the flyer please

Requirements
Must have
• My logo, my website , my phone number (to come later),
• FL State Lic. #CRC8047163 & Insured
• We Specialize in Bathroom and Kitchen remodeling ,new Construction & Interior or Exterior home Renovations, garages and more! Serving Central Florida for over 15 years.
• Family owned and operated,
• we perform all levels of building and remodeling.
• i wouldn't mind seeing what you come up with for text on the flyer.
Nice to have
• maybe a nice kitchen and bathroom pictures

```html
<!DOCTYPE html>
<html lang="en">
<head>
<meta charset="utf-8">
<title>Pine Hollow Builders Flyer</title>
<link href="https://fonts.googleapis.com/css2?family=Oswald:wght@400;500&family=Playfair+Display:wght@400;700&display=swap" rel="stylesheet">
<style>
  :root {
    --page-bg: #f1f0ec;
    --orange: #e0850d;
    --orange-light: #f3a63a;
    --orange-text: #f0920f;
    --ink: #2f2f2f;
    --grey-bar: #8a8a8a;
    --green: #4e6b4a;
    --white: #ffffff;
  }
  * { margin: 0; padding: 0; box-sizing: border-box; }
  html, body { width: 1200px; height: 1192px; overflow: hidden; background: var(--page-bg); }
  .flyer {
    position: absolute; left: 148px; top: 11px;
    width: 904px; height: 1170px; background: var(--white);
    font-family: "Oswald", sans-serif; color: var(--ink);
  }
  .hero {
    position: absolute; left: 0; top: 0; width: 904px; height: 470px;
    background: linear-gradient(180deg, #56709e 0%, #5d6478 35%, #6a5f5e 65%, #4d6a3e 100%);
  }
  .website {
    position: absolute; left: 34px; top: 22px;
    color: var(--white); font-size: 19px; font-weight: 500; letter-spacing: -0.3px;
  }
  .headline {
    position: absolute; left: 74px; top: 268px;
    font-family: "Playfair Display", serif; font-weight: 400;
    font-size: 104px; line-height: 90px; color: var(--orange-text);
    letter-spacing: -6px; transform: scaleX(0.86); transform-origin: left top;
    white-space: nowrap;
  }
  .band { position: absolute; left: 0; top: 470px; width: 904px; height: 20px; background: var(--orange-light); }
  .frame-side { position: absolute; top: 470px; width: 18px; height: 700px; background: var(--orange); }
  .frame-left { left: 0; }
  .frame-right { right: 0; }
  .frame-bottom { position: absolute; left: 0; top: 1150px; width: 904px; height: 20px; background: var(--orange); }
  .brand-tab { position: absolute; left: 548px; top: 1140px; width: 292px; height: 30px; background: var(--white); }
  .intro {
    position: absolute; left: 79px; top: 528px;
    font-size: 22px; line-height: 30px; letter-spacing: -0.2px;
  }
  .levels {
    position: absolute; left: 74px; top: 632px; width: 572px; height: 40px;
    background: var(--grey-bar); color: var(--white);
    font-size: 21px; line-height: 40px; padding-left: 16px; letter-spacing: 0.3px;
  }
  .badge { position: absolute; left: 688px; top: 518px; width: 144px; height: 164px; }
  .gallery-label {
    position: absolute; top: 702px; height: 22px;
    display: flex; align-items: center; gap: 10px;
    font-size: 16px; letter-spacing: 7px; font-weight: 500;
  }
  .gallery-label::before, .gallery-label::after { content: ""; flex: 1; height: 1px; background: var(--ink); }
  .label-kitchen { left: 74px; width: 379px; }
  .label-bath { left: 478px; width: 376px; }
  .photo { position: absolute; top: 729px; width: 185px; height: 123px; }
  .kitchen-before { left: 74px; background: linear-gradient(160deg, #8a5a2c, #c9b79a 60%, #5a3a22); }
  .kitchen-after { left: 268px; background: linear-gradient(160deg, #3a2a22, #9a8f86 55%, #d8d3cb); }
  .bath-before { left: 478px; background: linear-gradient(160deg, #e6e6e4, #b9b6ae 60%, #6a5a44); }
  .bath-after { left: 669px; background: linear-gradient(160deg, #8d948f, #c3c6c4 55%, #eceae6); }
  .caption {
    position: absolute; top: 860px; width: 185px; text-align: center;
    color: var(--orange); font-size: 16px; font-weight: 500; letter-spacing: 2.5px;
  }
  .services {
    position: absolute; left: 73px; top: 926px;
    font-size: 21px; line-height: 26px; text-transform: uppercase; letter-spacing: -0.2px;
  }
  .guarantee { position: absolute; left: 73px; top: 1027px; font-size: 22px; }
  .call {
    position: absolute; left: 73px; top: 1050px;
    font-family: "Playfair Display", serif; font-weight: 700;
    font-size: 46px; color: var(--orange); letter-spacing: -0.5px;
  }
  .license { position: absolute; left: 73px; top: 1101px; font-size: 22px; }
  .brand {
    position: absolute; left: 548px; top: 1060px; width: 292px;
    display: flex; flex-direction: column; align-items: center; gap: 12px;
  }
  .brand-mark { width: 56px; height: 56px; background: var(--orange); }
  .brand-name { font-size: 28px; font-weight: 500; color: #4a4a4a; letter-spacing: 1px; white-space: nowrap; }
</style>
</head>
<body>
<main class="flyer">
  <div class="hero" role="img" aria-label="Photo of a large brick two-storey home with gabled roof and front lawn"></div>
  <div class="website">www.brightmortarworks.example</div>
  <h1 class="headline">SOMTHING NEW<br>FOR YOUR HOME</h1>

  <div class="band"></div>
  <div class="frame-side frame-left"></div>
  <div class="frame-side frame-right"></div>
  <div class="frame-bottom"></div>
  <div class="brand-tab"></div>

  <p class="intro">We Specialize in Bathroom and Kitchen remodeling,<br>New Construction &amp; Interior or Exterior Home Renovations,<br>Garages &amp; more! Serving Central Florida for over 15 years.</p>
  <p class="levels">WE PERFORM ALL LEVELS OF BUILDING AND REMODELING.</p>

  <svg class="badge" viewBox="0 0 144 164" aria-label="Family owned and operated">
    <defs>
      <radialGradient id="shadow" cx="50%" cy="50%" r="50%">
        <stop offset="0" stop-color="#555" stop-opacity="0.7"/>
        <stop offset="1" stop-color="#555" stop-opacity="0"/>
      </radialGradient>
    </defs>
    <ellipse cx="72" cy="154" rx="70" ry="6" fill="url(#shadow)"/>
    <polygon fill="var(--green)" points="72,0 82,8 94,3 100,14 113,13 115,25 127,30 124,42 134,50 127,60 133,72 124,80 128,92 117,97 117,110 104,111 99,123 87,120 78,130 72,122 66,130 57,120 45,123 40,111 27,110 27,97 16,92 20,80 11,72 17,60 10,50 20,42 17,30 29,25 31,13 44,14 50,3 62,8"/>
    <text x="72" y="46" text-anchor="middle" fill="#fff" font-family="Oswald, sans-serif" font-size="20" font-weight="500">FAMILY</text>
    <text x="72" y="68" text-anchor="middle" fill="#fff" font-family="Oswald, sans-serif" font-size="20" font-weight="500">OWNED AND</text>
    <text x="72" y="90" text-anchor="middle" fill="#fff" font-family="Oswald, sans-serif" font-size="20" font-weight="500">OPERATED.</text>
  </svg>

  <div class="gallery-label label-kitchen">KITCHEN</div>
  <div class="gallery-label label-bath">BATHROOM</div>
  <div class="photo kitchen-before" role="img" aria-label="Kitchen before remodel with oak cabinets"></div>
  <div class="photo kitchen-after" role="img" aria-label="Kitchen after remodel with dark cabinets and stainless appliances"></div>
  <div class="photo bath-before" role="img" aria-label="Bathroom before remodel, stripped to subfloor"></div>
  <div class="photo bath-after" role="img" aria-label="Bathroom after remodel with tiled tub surround"></div>
  <div class="caption" style="left:74px">BEFORE</div>
  <div class="caption" style="left:268px">AFTER</div>
  <div class="caption" style="left:478px">BEFORE</div>
  <div class="caption" style="left:669px">AFTER</div>

  <p class="services">Our services: New Construction &nbsp;•&nbsp; Barns<br>Remodels &nbsp;•&nbsp; Renovations &nbsp;•&nbsp; Repairs<br>Kitchens &nbsp;•&nbsp; Bathrooms &nbsp;•&nbsp; Bank Remodels</p>
  <p class="guarantee">Quality Construction Guaranteed:</p>
  <p class="call">Call: 352-555-0186</p>
  <p class="license">FL State Lic. #CRC8047163 &amp; Insured</p>

  <div class="brand">
    <div class="brand-mark"></div>
    <div class="brand-name">PINE HOLLOW BUILDERS</div>
  </div>
</main>
</body>
</html>
```